Small environmental consultancy requires basic yet awesome website design by aspiring and cool desig

We are a small environmental consultancy based in Australia, we have set-out a design brief for our website, using a logo we had completed here on Mosaic Yard as well. We hope you can help us with a website!

Website must be pagelark friendly - we have reserved hosting with them already!

Number of Pages Required

4 page

Requirements
Must have
• use supplied logo
• pagelark
• follow provided brief

```html
<!DOCTYPE html>
<html lang="en">
<head>
<meta charset="utf-8">
<title>Verdant Advisors</title>
<link href="https://fonts.googleapis.com/css2?family=Open+Sans:wght@400;600;700&display=swap" rel="stylesheet">
<style>
:root{
  --green:#8cc63f;
  --green-dark:#5c9a2a;
  --ink:#444;
  --muted:#777;
  --grey-band:#e6e6e6;
  --footer:#3a3a3a;
  --footer-bottom:#2c2c2c;
  --white:#fff;
}
*{box-sizing:border-box;margin:0;padding:0}
html,body{width:870px;height:1200px;overflow:hidden}
body{font-family:"Open Sans",Arial,sans-serif;color:var(--ink);background:var(--white)}
.page{width:870px;height:1200px;display:flex;flex-direction:column}
.site-header{height:90px;flex:none;display:flex;align-items:center;justify-content:space-between;padding:0 80px 0 82px}
.brand{display:flex;align-items:center;gap:10px}
.brand-mark{width:40px;height:40px;border-radius:50%;background:var(--green)}
.brand-name{font-size:20px;font-weight:600;color:var(--green-dark);line-height:1}
.main-nav{display:flex;gap:22px}
.main-nav a{font-size:11px;color:var(--ink);text-decoration:none;letter-spacing:.5px}
.hero{height:300px;flex:none;position:relative;background:radial-gradient(ellipse at 50% 40%,#f3fbe3 0%,#b8e07a 35%,#6fb52e 70%,#3f8a1c 100%)}
.hero-quote{position:absolute;left:198px;top:100px;width:470px;padding:16px 22px;background:rgba(255,255,255,.72);font-size:15px;line-height:1.4;color:#333;text-align:center}
.hero-dots{position:absolute;left:82px;bottom:22px;display:flex;gap:6px}
.hero-dots span{width:8px;height:8px;border-radius:50%;background:var(--white);opacity:.85}
.partners{height:95px;flex:none;display:flex;align-items:center;justify-content:center;gap:22px}
.partner-badge{width:92px;height:40px;background:#d5d5d5;border-radius:3px}
.partner-badge:nth-child(odd){background:#c9d8bb}
.about{background:var(--grey-band);height:195px;flex:none;text-align:center;padding-top:16px}
.section-title{font-size:19px;font-weight:400;color:var(--green);letter-spacing:.5px;line-height:26px}
.directors{display:flex;justify-content:center;gap:14px;margin:12px 0}
.director-photo{width:60px;height:60px;background:linear-gradient(#8a7d6e,#5d5248)}
.about p{width:560px;margin:0 auto;font-size:11px;line-height:1.6;color:var(--muted)}
.services{height:270px;flex:none;padding-top:22px;text-align:center}
.services .intro{width:700px;margin:10px auto 16px;font-size:11px;line-height:1.6;color:var(--muted);text-align:left}
.service-list{display:flex;justify-content:center;gap:24px}
.service{width:170px;display:flex;flex-direction:column;align-items:center}
.service-icon{width:66px;height:66px;border-radius:50%;border:2px solid #ddd;display:flex;align-items:center;justify-content:center;background:var(--white)}
.service-icon.active{background:var(--green);border-color:var(--green)}
.service span{margin-top:8px;font-size:11px;line-height:1.4;color:var(--ink)}
.site-footer{height:250px;flex:none;position:relative;background:var(--footer);color:#ccc}
.footer-cols{display:flex;padding:26px 82px 0}
.footer-col{width:270px}
.footer-col h3{font-size:14px;font-weight:400;color:var(--white);margin-bottom:10px}
.footer-col li{list-style:none;font-size:10px;line-height:1.8}
.social{display:flex;gap:6px}
.social span{width:18px;height:18px;border-radius:3px;background:#7fa8d8}
.social span:last-child{background:#ddd}
.footer-bottom{position:absolute;left:0;bottom:0;width:870px;height:30px;background:var(--footer-bottom);font-size:9px;color:#999;text-align:center;line-height:30px}
</style>
</head>
<body>
<div class="page">
  <header class="site-header">
    <div class="brand"><div class="brand-mark"></div><span class="brand-name">Verdant Advisors</span></div>
    <nav class="main-nav"><a href="#">HOME</a><a href="#">SERVICES</a><a href="#">PEOPLE</a><a href="#">CLIENTS</a><a href="#">CONTACT</a></nav>
  </header>

  <section class="hero" role="img" aria-label="Young green seedling growing against a soft bright green background">
    <p class="hero-quote">Verdant Advisors is Client focussed, offering highly experienced consultants, providing effective and innovative environmental solutions.</p>
    <div class="hero-dots"><span></span><span></span><span></span><span></span></div>
  </section>

  <section class="partners" aria-label="Clients">
    <div class="partner-badge"></div><div class="partner-badge"></div><div class="partner-badge"></div><div class="partner-badge"></div><div class="partner-badge"></div><div class="partner-badge"></div>
  </section>

  <section class="about">
    <h2 class="section-title">ABOUT COMPANY</h2>
    <div class="directors">
      <div class="director-photo" role="img" aria-label="Portrait of director Daniel Marsh"></div>
      <div class="director-photo" role="img" aria-label="Portrait of director Peter Lowry"></div>
    </div>
    <p>Formed by Directors Daniel Marsh and Peter Lowry, Verdant Advisors brings to the table a wealth of experience combined with the responsiveness and reliability of a smaller company.</p>
  </section>

  <section class="services">
    <h2 class="section-title">OUR SERVICES</h2>
    <p class="intro">We offer a range of environmental services including Project Management, Contaminated Land Assessment and Remediation, Hazardous Materials and Occupational Hygiene, and related Environmental Assessment and Management Services.</p>
    <div class="service-list">
      <div class="service"><div class="service-icon active"><svg width="30" height="30" viewBox="0 0 30 30"><circle cx="15" cy="12" r="7" fill="none" stroke="#fff" stroke-width="2"/><rect x="12" y="20" width="6" height="5" fill="#fff"/></svg></div><span>Project management</span></div>
      <div class="service"><div class="service-icon"><svg width="30" height="30" viewBox="0 0 30 30"><path d="M15 25C6 22 6 10 15 5C24 10 24 22 15 25Z" fill="var(--green)"/></svg></div><span>Contaminated Land Assessment<br>and Remediation</span></div>
      <div class="service"><div class="service-icon"><svg width="30" height="30" viewBox="0 0 30 30"><rect x="7" y="5" width="16" height="21" rx="2" fill="none" stroke="var(--green)" stroke-width="2"/><path d="M11 12h8M11 16h8M11 20h5" stroke="var(--green)" stroke-width="2"/></svg></div><span>Hazardous Materials and<br>Occupational Hygiene</span></div>
      <div class="service"><div class="service-icon"><svg width="30" height="30" viewBox="0 0 30 30"><rect x="5" y="7" width="20" height="16" fill="none" stroke="var(--green)" stroke-width="2"/><path d="M7 21l6-7 4 4 3-3 4 6" fill="none" stroke="var(--green)" stroke-width="2"/></svg></div><span>Environmental Assessment and<br>Management Services</span></div>
    </div>
  </section>

  <footer class="site-footer">
    <div class="footer-cols">
      <div class="footer-col"><h3>Quick Links</h3><ul><li>Home</li><li>Services</li><li>People</li><li>Clients</li><li>Contact Us</li></ul></div>
      <div class="footer-col"><h3>Contact Us</h3><ul><li>Level 4, 210 Harbour Street</li><li>Brisbane QLD 4000</li><li>p. 07 5550 1234</li><li>info@verdantadvisors.example</li></ul></div>
      <div class="footer-col"><h3>Follow Us</h3><div class="social"><span></span><span></span><span></span><span></span></div></div>
    </div>
    <div class="footer-bottom">© 2024 Verdant Advisors. All rights reserved.</div>
  </footer>
</div>
</body>
</html>
```